Sticker label for natural moisturizer

I need a sticker label designed for a homemade moisturizer made from beef tallow and honey.
Must include: Logo, product name (Classic Suet & Clover Balm), ingredients (in English and Polish, can use placeholder text for initial design), brief description of product with instructions for use (in English and Polish, can use placeholder text for initial design), manufacturer name (vorelmart.com), manufacturer address (placeholder text for initial design), volume of container (60ml / 2oz)
The product is used by both males and females of all ages, so must be unisex design with broad appeal.
Dimensions: Length 15cm, Height 3cm
Style: Has to simultaneously communicate that this is a homemade product with no chemical fillers AND that it is of extremely high quality.
Brand colors:
#57665C
#FCFAF6
#FFFFFF
#000000
#B99B83
#EAE4DD
#CC8E5A

```html
<!DOCTYPE html>
<html lang="en">
<head>
<meta charset="utf-8">
<title>Classic Suet &amp; Clover Balm – Label</title>
<link href="https://fonts.googleapis.com/css2?family=Cinzel:wght@400;600;700&family=Josefin+Slab:wght@400;600&family=Mulish:wght@500&family=Spectral+SC:wght@500&display=swap" rel="stylesheet">
<style>
  :root{
    --sage:#57665C;
    --ink:#1b1b1b;
    --paper:#ECE8DC;
    --paper-deep:#E4DFD1;
    --canvas:#F4F3F0;
    --muted:#8d918a;
  }
  *{box-sizing:border-box;margin:0;padding:0}
  html,body{width:1200px;height:960px;overflow:hidden;background:var(--canvas)}
  .stage{width:1200px;height:960px;display:flex;align-items:center;justify-content:center}
  .label{position:relative;width:1140px;height:228px;color:var(--ink)}
  .label__paper{position:absolute;inset:0;background:linear-gradient(135deg,var(--paper) 0%,var(--paper-deep) 100%)}
  .label__content{position:absolute;inset:0}

  .description{position:absolute;left:22px;top:20px;width:222px;text-align:center;font-family:"Cinzel",serif;font-size:13.5px;line-height:16.6px;color:var(--ink)}
  .description--pl{top:116px;color:var(--muted);font-size:13.5px}

  .brand{position:absolute;left:0;right:0;top:14px;text-align:center;font-family:"Mulish",sans-serif;font-weight:500;font-size:25px;letter-spacing:.2px;color:var(--ink)}

  .product{position:absolute;left:385px;top:87px;width:367px;height:65px;border:1.5px solid var(--sage);display:flex;align-items:center;justify-content:center}
  .product__top,.product__bottom{position:absolute;left:50%;transform:translateX(-50%);background:var(--paper);padding:0 6px;font-family:"Cinzel",serif;font-weight:600;font-size:15px;letter-spacing:6px;color:var(--sage);white-space:nowrap;line-height:1}
  .product__top{top:-9px}
  .product__bottom{bottom:-9px}
  .product__name{font-family:"Cinzel",serif;font-weight:700;font-size:34px;color:var(--sage);letter-spacing:.3px;white-space:nowrap}

  .subline{position:absolute;left:0;right:0;top:184px;text-align:center;font-family:"Spectral SC",serif;font-weight:500;font-size:10.5px;letter-spacing:1px}
  .volume{position:absolute;left:0;right:0;top:200px;text-align:center;font-family:"Josefin Slab",serif;font-size:10.5px}

  .details{position:absolute;left:900px;top:20px;width:226px;font-family:"Josefin Slab",serif;font-size:13.5px;line-height:16.6px}
  .details b{font-weight:600;letter-spacing:-.2px}
  .details__en{color:var(--muted)}
  .details__pl{color:#a6a9a2;margin-top:2px}
  .details__pl b,.details__en b{color:var(--ink)}
  .details__maker{margin-top:2px;color:var(--ink)}
</style>
</head>
<body>
<main class="stage">
  <section class="label" aria-label="Classic Suet &amp; Clover Balm sticker label">
    <div class="label__paper" role="img" aria-label="Cream paper background with a faint honeycomb texture"></div>
    <div class="label__content">
      <p class="description">A beautiful rich Suet &amp; Clover Balm with NO Chemical Fillers &amp; of extremely high quality</p>
      <p class="description description--pl">Piękny, bogaty balsam łojowo-koniczynowy BEZ chemicznych wypełniaczy ORAZ wyjątkowo wysokiej jakości</p>

      <div class="brand">vorel</div>

      <div class="product">
        <span class="product__top">CLASSIC</span>
        <span class="product__name">SUET &amp; CLOVER</span>
        <span class="product__bottom">BALM</span>
      </div>

      <p class="subline">Klasyczny ŁÓJ I KONICZYNA Balsam</p>
      <p class="volume">60ml / 2oz</p>

      <div class="details">
        <p class="details__en"><b>Ingredients:</b> 100% Grass Finished Beef Tallow, Jojoba Oil, Manuka Oil, Calendula Oil, Orange Essential Oil, and Lavender Oil</p>
        <p class="details__pl"><b>Składniki:</b> 100% łój wołowy z trawy, olej jojoba, olej manuka, olejek z nagietka, olejek eteryczny pomarańczowy i olejek lawendowy</p>
        <p class="details__maker"><b>Manufactured by:</b> www.vorelmart.com<br>address, city, country, postal code</p>
      </div>
    </div>
  </section>
</main>
</body>
</html>
```